Medical Transportation Company Brochure

I need a brochure for a medical transportation company called CareVanta Mobile Health Services that provides ambulance and mobility assistance vehicle transportation services to and from healthcare facilities as well as event standby and healthcare training through our training center (cpr, professional continuing education courses). Id like something that incorporates our company logo's colors and looks eye catching yet sleek and professional

Target Market(s)

Patients, healthcare facilities

Industry/Entity Type

Medical

Font styles to use
Sans Serif

Requirements
Must have
• Flyer must have a description of our services as well as text that is easy to read, be visually captivating and stand out, include our contact information and process to book appointment for transport with us

```html
<!DOCTYPE html>
<html lang="en">
<head>
<meta charset="utf-8">
<title>CareVanta Trifold Brochure</title>
<link rel="stylesheet" href="https://fonts.googleapis.com/css2?family=Oswald:wght@500;600&family=Raleway:wght@400;500&family=Hind:wght@400;500;600&display=swap">
<style>
  :root {
    --navy: #1c3370;
    --navy-deep: #17244f;
    --red: #c8102e;
    --ink: #1f2433;
    --paper: #f6f6f7;
    --paper-grey: #dedfe3;
    --stage: #e4e4e6;
    --muted: #cfd5e6;
  }
  * { box-sizing: border-box; margin: 0; padding: 0; }
  html, body { width: 800px; height: 1200px; overflow: hidden; background: var(--stage); }
  body { position: relative; font-family: "Hind", sans-serif; color: var(--ink); }

  .spread { position: absolute; left: 14px; width: 772px; height: 578px; display: flex; box-shadow: 0 10px 24px rgba(0,0,0,.18); }
  .spread--outside { top: 8px; }
  .spread--inside { top: 612px; }
  .panel { position: relative; width: 33.333%; height: 100%; overflow: hidden; background: var(--paper); }

  .head { font-family: "Oswald", sans-serif; font-weight: 600; text-transform: uppercase; line-height: 1.02; color: var(--navy); letter-spacing: -.6px; }
  .head .accent { color: var(--red); }

  .photo { position: absolute; }

  /* outside spread */
  .grow-band { position: absolute; left: 0; top: 0; width: 100%; height: 128px; background: var(--navy); padding: 10px 12px; color: #fff; }
  .grow-band .head { color: #fff; font-size: 25px; }
  .grow-band p { font-family: "Raleway", sans-serif; font-size: 10.5px; line-height: 1.5; margin-top: 5px; }
  .panel--best .photo { left: 10px; top: 128px; width: 247px; height: 170px; background: linear-gradient(135deg, #aebfd3, #e7ecf1 55%, #8e99a8); }
  .best-copy { position: absolute; top: 306px; left: 10px; right: 10px; }
  .best-copy .head { font-size: 25px; }
  .best-copy p { font-family: "Raleway", sans-serif; font-size: 10px; line-height: 1.55; margin-top: 5px; }
  .steps { list-style: none; margin-top: 6px; counter-reset: step; }
  .steps li { font-family: "Raleway", sans-serif; font-size: 10px; line-height: 1.45; padding-left: 20px; position: relative; margin-bottom: 5px; counter-increment: step; }
  .steps li::before { content: counter(step); position: absolute; left: 0; top: 1px; width: 14px; height: 14px; border-radius: 50%; background: var(--red); color: #fff; font-size: 9px; line-height: 14px; text-align: center; font-weight: 500; }
  .steps strong { color: var(--navy); font-weight: 500; }

  .panel--touch { background: var(--paper-grey); }
  .panel--touch .photo { left: 10px; top: 8px; width: 240px; height: 300px; background: linear-gradient(160deg, #6a3a2e, #8a4a38 40%, #3c3b41 75%, #23262d); }
  .touch-title { position: absolute; top: 338px; width: 100%; text-align: center; font-size: 32px; }
  .contact { position: absolute; left: 30px; right: 14px; top: 395px; list-style: none; }
  .contact li { display: flex; gap: 14px; align-items: flex-start; font-size: 13.5px; line-height: 1.3; margin-bottom: 15px; }
  .contact svg { width: 22px; height: 22px; flex: none; margin-top: 2px; }

  .panel--intro { background: #fff; }
  .intro-frame { position: absolute; left: 0; top: 0; width: 100%; height: 240px; background: var(--navy); }
  .panel--intro .photo { left: 0; top: 8px; width: 252px; height: 248px; background: linear-gradient(120deg, #c2c7cf, #eef0f3 45%, #b0322f 62%, #3a3d48 80%); }
  .intro-copy { position: absolute; top: 280px; left: 10px; right: 12px; }
  .intro-copy .head { font-size: 33px; line-height: 1.12; }
  .intro-copy p { font-size: 12.5px; line-height: 1.5; margin-top: 12px; }
  .brand { display: flex; align-items: center; gap: 8px; margin: 16px 0 0 12px; }
  .brand-dot { width: 26px; height: 26px; border-radius: 50%; background: var(--navy); }
  .brand-name { font-family: "Oswald", sans-serif; font-weight: 600; font-size: 28px; color: var(--red); line-height: 1; }

  /* inside spread */
  .panel--services-list { background: #fff; }
  .panel--services-list .photo { left: 16px; top: 0; width: 232px; height: 168px; background: linear-gradient(135deg, #4d6a4a, #d9d4c9 45%, #eceff1 70%, #7c8088); }
  .list-copy { position: absolute; top: 178px; left: 16px; right: 10px; }
  .list-copy .head { font-size: 22px; white-space: nowrap; }
  .rule { width: 150px; height: 2px; background: var(--navy); margin: 4px 0 6px; }
  .list-copy p { font-size: 9.5px; line-height: 1.6; }
  .item { margin-top: 10px; }
  .item h3 { font-family: "Raleway", sans-serif; font-weight: 500; font-size: 13px; color: var(--navy); text-transform: uppercase; line-height: 1.2; margin-bottom: 2px; }
  .item h3 .accent { color: var(--red); }

  .panel--our-services { background: var(--navy-deep); color: #fff; text-align: center; padding: 14px 14px 0; }
  .panel--our-services > .head { color: #fff; font-size: 30px; font-weight: 500; }
  .panel--our-services > p { font-size: 9.5px; line-height: 1.6; color: var(--muted); margin-top: 8px; }
  .svc { background: rgba(255,255,255,.04); margin-top: 12px; padding: 11px 12px 10px; }
  .svc .head { color: #fff; font-size: 14.5px; font-weight: 500; }
  .svc p { font-size: 9px; line-height: 1.65; color: var(--muted); margin-top: 6px; }

  .panel--why { background: var(--paper); }
  .panel--why .photo { left: 10px; top: 2px; width: 236px; height: 216px; background: linear-gradient(120deg, #3b3630, #8d8a86 40%, #e8eaed 60%, #2d4fa0 80%, #4e5d39); }
  .why-copy { position: absolute; top: 232px; left: 10px; right: 30px; }
  .why-copy .head { font-size: 25px; }
  .why-copy .rule { width: 112px; }
  .why-copy p { font-size: 9.5px; line-height: 1.6; text-align: justify; margin-top: 10px; }
  .why-copy p.tight { margin-top: 0; }
</style>
</head>
<body>

<section class="spread spread--outside">
  <div class="panel panel--best">
    <div class="grow-band">
      <h2 class="head">We help to grow</h2>
      <p>Beyond transport, our crews provide event standby for races and gatherings, and our training center runs CPR and continuing education courses.</p>
    </div>
    <div class="photo" role="img" aria-label="Paramedic on a motorcycle beside a runner at a road race"></div>
    <div class="best-copy">
      <h2 class="head">Book your <span class="accent">ride</span></h2>
      <p>Booking a transport with CareVanta takes three simple steps:</p>
      <ol class="steps">
        <li><strong>Call or email us</strong> with the patient's name, pickup address and destination.</li>
        <li><strong>Choose a vehicle</strong>: ambulance or mobility assistance van, plus date and time.</li>
        <li><strong>Get confirmation</strong> from a coordinator with your crew and arrival window.</li>
      </ol>
    </div>
  </div>

  <div class="panel panel--touch">
    <div class="photo" role="img" aria-label="Ambulance on a city street with brick buildings and a cyclist"></div>
    <h2 class="head touch-title">Get in <span class="accent">touch</span></h2>
    <ul class="contact">
      <li>
        <svg viewBox="0 0 24 24" fill="none" stroke="#1c3370" stroke-width="2" stroke-linecap="round" stroke-linejoin="round"><path d="M5 3h4l2 5-2.5 1.5a11 11 0 0 0 6 6L16 13l5 2v4a2 2 0 0 1-2 2A16 16 0 0 1 3 5a2 2 0 0 1 2-2z"/><path d="M15 3a6 6 0 0 1 6 6M15 7a2 2 0 0 1 2 2"/></svg>
        <span>+1 555 014 2200<br>+1 555 014 2201</span>
      </li>
      <li>
        <svg viewBox="0 0 24 24" fill="none" stroke="#1c3370" stroke-width="2"><circle cx="12" cy="12" r="9"/><path d="M3 12h18M12 3c3 3 3 15 0 18M12 3c-3 3-3 15 0 18"/></svg>
        <span>hello@carevanta.com<br>www.carevanta.com</span>
      </li>
      <li>
        <svg viewBox="0 0 24 24" fill="#1c3370"><path d="M12 3 2 12h3v9h5v-6h4v6h5v-9h3z"/></svg>
        <span>48 Harbor Lane, 2nd Floor<br>Riverton, NY 10450</span>
      </li>
    </ul>
  </div>

  <div class="panel panel--intro">
    <div class="intro-frame"></div>
    <div class="photo" role="img" aria-label="Close view of an ambulance van in motion"></div>
    <div class="intro-copy">
      <h1 class="head">Mobile health<br>services <span class="accent">that<br>provides.</span></h1>
      <p>CareVanta Mobile Health Services that provides ambulance and mobility assistance vehicle transportation services to and from healthcare facilities.</p>
      <div class="brand"><span class="brand-dot"></span><span class="brand-name">CareVanta</span></div>
    </div>
  </div>
</section>

<section class="spread spread--inside">
  <div class="panel panel--services-list">
    <div class="photo" role="img" aria-label="Ambulances parked outside a hospital entrance"></div>
    <div class="list-copy">
      <h2 class="head">Mobile health <span class="accent">services</span></h2>
      <div class="rule"></div>
      <p>We have an excellent team of drivers, patient care managers, and management staff. They work together to provide you with the most complete bedside-to-bedside service.</p>
      <div class="item"><h3>Ambulance</h3><p>Whether it is to or from their home, nursing home, assisted living facility doctor's office or hospital.</p></div>
      <div class="item"><h3>Mobility assistance <span class="accent">vehicle</span></h3><p>were chosen for their ability to provide non-ambulatory patients with maximum comfort.</p></div>
      <div class="item"><h3>Event <span class="accent">standby</span></h3><p>trained crews and a ready vehicle on site for races, games, concerts and community events.</p></div>
      <div class="item"><h3>Training <span class="accent">center</span></h3><p>CPR certification and professional continuing education courses taught by our experienced staff.</p></div>
    </div>
  </div>

  <div class="panel panel--our-services">
    <h2 class="head">Our services</h2>
    <p>we offers the very best service in nationwide long distance and non-emergency medical transportation (NEMT) ground services.</p>
    <div class="svc"><h3 class="head">Long distance patient transport</h3><p>medical transportation company. We offer state to state patient transport for non- emergency situations.</p></div>
    <div class="svc"><h3 class="head">Trust our qualified staff</h3><p>We offer an experienced team of drivers, nurses and patient care managers who work together to provide the most comfortable. experience.</p></div>
    <div class="svc"><h3 class="head">Luxury, comfort &amp; safety</h3><p>Our long distance medical vans are fully equipped to meet your needs and ensure the most comfortable ride.</p></div>
    <div class="svc"><h3 class="head">We will take care of everything</h3><p>All it takes is one call and everything will be taken care of. Our transport coordinators are standing by 24/7...</p></div>
  </div>

  <div class="panel panel--why">
    <div class="photo" role="img" aria-label="Ambulance driving fast along a street"></div>
    <div class="why-copy">
      <h2 class="head">Why choose <span class="accent">us</span></h2>
      <div class="rule"></div>
      <p>We are revolutionizing the non-emergency medical transport industry by utilizing some of the most cost effective ground transport services and equipment that are specially configured as mobile intensive care units.</p>
      <p>All of our medical vehicles are the largest, most spacious medical ground transportation vehicles in the industry.</p>
      <p>non-emergency transportation state to state to and from hospitals, doctor's facilities, and patient's homes.</p>
      <p class="tight">Listed here are just a few reasons why CareVanta has quickly become the experienced choice in medical transportation: Largest Fleet Medical Transportation Vans Nationwide ..</p>
    </div>
  </div>
</section>

</body>
</html>
```